Offshore Energy Projects Management Consultancy needs a business card design

Logo available. We provide teams to deliver engineering consultancy, project management and delivery teams mainly in the offshore renewables sector. The company is all about bringing the right people to a project to deliver the scope.

The business card will be used for all staff.

The business card should be quite simple, vibrant and uncluttered but convey experience, enthusiasm and integration.

Target Market(s)

Energy Project Developers and Tier 1 construction companies

Contact Information for Business Card

Logo should be on the back of the card. I'm happy for the designer to play with the colour of the logo and background colour.

Front of the card should convey all the must have information in a clear and professional manner but without being overly traditional.

Colors

Designer to choose colors to be used in the design.

Requirements
Must have
• Land Line Tel Number, Mobile Tel Number, Email, business address, web address.

```html
<!DOCTYPE html>
<html lang="en">
<head>
<meta charset="utf-8">
<title>Seaward Delivery Partners – Business Card</title>
<link href="https://fonts.googleapis.com/css2?family=Open+Sans:wght@400;600;700&family=Montserrat:wght@800&display=swap" rel="stylesheet">
<style>
  :root {
    --stage: #161616;
    --card: #212121;
    --blue: #1778c8;
    --blue-light: #2aa3e0;
    --white: #ffffff;
    --text: #f2f2f2;
  }
  * { box-sizing: border-box; margin: 0; padding: 0; }
  html, body { width: 1200px; height: 900px; overflow: hidden; }
  body {
    background: var(--stage);
    font-family: "Open Sans", Arial, sans-serif;
    display: flex;
    flex-direction: column;
    align-items: center;
    justify-content: center;
    gap: 44px;
  }
  .card {
    position: relative;
    width: 740px;
    height: 400px;
    background: var(--card);
    overflow: hidden;
  }
  .card::after {
    content: "";
    position: absolute;
    left: 0; right: 0; bottom: 0;
    height: 9px;
    background: var(--blue);
  }

  /* Back: company name */
  .card-back {
    display: flex;
    align-items: center;
    justify-content: center;
  }
  .brand {
    display: flex;
    align-items: center;
    gap: 18px;
  }
  .brand-dot {
    width: 34px; height: 34px;
    border-radius: 50%;
    background: var(--blue-light);
    flex: none;
  }
  .brand-name {
    font-weight: 700;
    color: var(--white);
    font-size: 40px;
    line-height: 1.1;
    text-transform: uppercase;
    letter-spacing: 0.5px;
  }
  .brand-name.small { font-size: 30px; }

  /* Front: details */
  .card-front {
    display: flex;
    align-items: center;
  }
  .card-front .brand {
    width: 400px;
    justify-content: center;
    padding-left: 20px;
  }
  .divider {
    width: 2px;
    height: 250px;
    background: var(--blue);
    margin-right: 30px;
  }
  .details { color: var(--text); }
  .person-name {
    font-family: "Montserrat", Arial, sans-serif;
    font-weight: 800;
    font-size: 27px;
    color: var(--blue);
    letter-spacing: 0.5px;
    line-height: 1.05;
  }
  .person-role { font-size: 17px; margin-bottom: 22px; }
  .address { font-size: 16px; line-height: 1.3; margin-bottom: 22px; }
  .contact-list { list-style: none; font-size: 16px; }
  .contact-list li {
    display: flex;
    align-items: center;
    gap: 12px;
    line-height: 1.6;
  }
  .contact-list svg { width: 18px; height: 18px; flex: none; }
</style>
</head>
<body>

  <section class="card card-back">
    <div class="brand">
      <span class="brand-dot"></span>
      <div class="brand-name">Seaward Delivery<br>Partners</div>
    </div>
  </section>

  <section class="card card-front">
    <div class="brand">
      <span class="brand-dot"></span>
      <div class="brand-name small">Seaward Delivery<br>Partners</div>
    </div>
    <div class="divider"></div>
    <div class="details">
      <div class="person-name">Rowan Talbeck</div>
      <div class="person-role">Managing Director</div>
      <div class="address">The Harbourview building,<br>212 Quay Road,<br>Portlen, PL4 7XY, Uk</div>
      <ul class="contact-list">
        <li>
          <svg viewBox="0 0 24 24" fill="#1778c8" aria-hidden="true"><path d="M6.6 10.8a15.1 15.1 0 0 0 6.6 6.6l2.2-2.2c.3-.3.7-.4 1-.2 1.1.4 2.3.6 3.6.6.6 0 1 .4 1 1V20c0 .6-.4 1-1 1A17 17 0 0 1 3 4c0-.6.4-1 1-1h3.5c.6 0 1 .4 1 1 0 1.3.2 2.5.6 3.6.1.3 0 .7-.2 1z"/></svg>
          +44 (0)1632 960412
        </li>
        <li>
          <svg viewBox="0 0 24 24" fill="none" stroke="#1778c8" stroke-width="2" aria-hidden="true"><rect x="6" y="2" width="12" height="20" rx="2"/><line x1="11" y1="18" x2="13" y2="18"/></svg>
          +44(0)7700 900318
        </li>
        <li>
          <svg viewBox="0 0 24 24" fill="none" stroke="#1778c8" stroke-width="2" aria-hidden="true"><rect x="2" y="5" width="20" height="14"/><polyline points="2,5 12,13 22,5"/></svg>
          R.Talbeck@seawarddp.ltd
        </li>
        <li>
          <svg viewBox="0 0 24 24" fill="none" stroke="#1778c8" stroke-width="2" aria-hidden="true"><circle cx="12" cy="12" r="10"/><ellipse cx="12" cy="12" rx="4.5" ry="10"/><line x1="2" y1="12" x2="22" y2="12"/></svg>
          www.seawarddp.ltd
        </li>
      </ul>
    </div>
  </section>

</body>
</html>
```